Brochure design for garden shed range for www.yardhuts2go.ie

we want to have a brochure designed for our products at www.yardhuts2go.ie
this should clearly show the ranges of products we sell and there features it wont need all our pricing but more to show our quality of products. We can work together with designers to get the right information on all our ranges and any text needed for the brochure.

Target Market(s)

general public

Industry/Entity Type

Home And Garden

```html
<!DOCTYPE html>
<html lang="en">
<head>
<meta charset="utf-8">
<title>Yard Huts 2 Go – Garden Shed Range</title>
<link rel="stylesheet" href="https://fonts.googleapis.com/css2?family=EB+Garamond:wght@500&family=Open+Sans:wght@400;700&display=swap">
<style>
  :root {
    --green-dark: #0c3a14;
    --olive: #5e6c1a;
    --panel: #ececec;
    --panel-edge: #f6f6f6;
    --ink: #2b2b2b;
    --ink-soft: #444;
    --white: #ffffff;
    --wood-warm-1: #b5702c;
    --wood-warm-2: #d89a55;
    --wood-pale-1: #c9c19a;
    --wood-pale-2: #e3dcc0;
    --grass: #5d7a3a;
    --sky: #c8d5de;
  }
  * { box-sizing: border-box; margin: 0; padding: 0; }
  html, body { width: 1200px; height: 849px; overflow: hidden; background: var(--white); }
  .brochure { position: relative; width: 1200px; height: 849px; background: var(--white); font-family: "Open Sans", Arial, sans-serif; }

  .product-card { position: absolute; width: 336px; height: 176px; }
  .product-card__title {
    height: 37px; background: var(--green-dark); color: var(--white);
    border-radius: 14px 14px 0 0; text-align: center;
    font-family: "EB Garamond", Georgia, serif; font-weight: 500; font-size: 29px; line-height: 37px;
  }
  .product-card__body {
    position: relative; height: 139px; overflow: hidden;
    background: linear-gradient(90deg, var(--panel), var(--panel-edge));
    border-radius: 0 0 14px 14px;
  }
  .product-card__photo {
    position: absolute; left: 0; top: 0; width: 215px; height: 139px;
    -webkit-mask-image: linear-gradient(90deg, #000 70%, transparent 100%);
    mask-image: linear-gradient(90deg, #000 70%, transparent 100%);
  }
  .photo--warm { background: linear-gradient(180deg, var(--sky) 0%, var(--wood-warm-2) 25%, var(--wood-warm-1) 75%, var(--grass) 100%); }
  .photo--pale { background: linear-gradient(180deg, var(--sky) 0%, var(--wood-pale-2) 25%, var(--wood-pale-1) 80%, #8a8a80 100%); }

  .product-card__price {
    position: absolute; left: 0; top: 117px; width: 152px; height: 27px;
    background: var(--olive); color: var(--white); border-radius: 0 14px 14px 0;
    font-weight: 700; font-size: 13px; line-height: 27px; padding-left: 18px;
  }
  .product-card__features {
    position: absolute; left: 172px; top: 17px; width: 164px;
    font-size: 12.6px; line-height: 14.2px; color: var(--ink-soft);
  }
  .product-card__features h3 { font-size: 12.6px; font-weight: 700; color: var(--ink); }
  .product-card__features ul { list-style: none; }
  .product-card__features li { position: relative; padding-left: 13px; }
  .product-card__features li::before { content: ""; position: absolute; left: 1px; top: 5px; width: 5px; height: 5px; background: var(--ink-soft); }

  .col-1 { left: 32px; } .col-2 { left: 432px; } .col-3 { left: 832px; }
  .row-1 { top: 25px; } .row-2 { top: 219px; } .row-3 { top: 412px; } .row-4 { top: 606px; }

  .brand-mark { position: absolute; left: 822px; top: 640px; width: 150px; display: flex; align-items: center; gap: 8px;
    font-family: "Open Sans", Arial, sans-serif; font-weight: 700; font-size: 17px; line-height: 19px; color: var(--green-dark); }
  .brand-mark__square { width: 22px; height: 22px; background: #c0392b; flex: none; }
  .partner-mark { position: absolute; left: 982px; top: 645px; width: 110px; text-align: center;
    font-weight: 700; font-size: 17px; color: #1f3a8a; }
  .cert-badge { position: absolute; left: 836px; top: 728px; }

  .footer-band { position: absolute; left: 0; top: 808px; width: 1200px; height: 41px; background: var(--green-dark);
    color: var(--white); text-align: center; font-weight: 700; font-size: 20px; line-height: 41px; letter-spacing: 0.2px; }
</style>
</head>
<body>
<main class="brochure">

  <article class="product-card col-1 row-1">
    <h2 class="product-card__title">Premium Standard</h2>
    <div class="product-card__body">
      <div class="product-card__photo photo--warm" role="img" aria-label="Photo of a timber apex garden shed with windows"></div>
      <div class="product-card__features"><h3>Product Features</h3><ul>
        <li>Shiplap Siding</li><li>T&amp;G Roof &amp; Floor</li><li>TimberTone Treated</li><li>Glazed Windows</li><li>Heavy Duty Felt Roof</li><li>Free Fitting &amp; Delivery</li></ul></div>
      <p class="product-card__price">From €499.99</p>
    </div>
  </article>

  <article class="product-card col-2 row-1">
    <h2 class="product-card__title">Premium Lean</h2>
    <div class="product-card__body">
      <div class="product-card__photo photo--warm" role="img" aria-label="Photo of a timber lean-to shed"></div>
      <div class="product-card__features"><h3>Product Features</h3><ul>
        <li>Shiplap Siding</li><li>TimberTone Treated</li><li>T&amp;G Floor and Roof</li><li>Galvanised Nailed</li><li>90lb Felt Roof Menbrane</li></ul></div>
      <p class="product-card__price">From €349.99</p>
    </div>
  </article>

  <article class="product-card col-3 row-1">
    <h2 class="product-card__title">Potting Sheds</h2>
    <div class="product-card__body">
      <div class="product-card__photo photo--warm" role="img" aria-label="Photo of a timber potting shed with many windows"></div>
      <div class="product-card__features"><h3>Product Features</h3><ul>
        <li>Shiplap Siding</li><li>TimberTone Treated</li><li>T&amp;G Floor and Roof</li><li>Galvanised Nailed</li><li>90lb Felt Roof Menbrane</li></ul></div>
      <p class="product-card__price">From €549.00</p>
    </div>
  </article>

  <article class="product-card col-1 row-2">
    <h2 class="product-card__title">Premium Kendal</h2>
    <div class="product-card__body">
      <div class="product-card__photo photo--warm" role="img" aria-label="Photo of a timber Kendal style shed"></div>
      <div class="product-card__features"><h3>Product Features</h3><ul>
        <li>T&amp;G Floor and roof</li><li>Shiplap Siding</li><li>Glazed windows</li><li>TimberTone Treated</li><li>Galavanised Fitting</li><li>Free home delivery</li></ul></div>
      <p class="product-card__price">From €479.99</p>
    </div>
  </article>

  <article class="product-card col-2 row-2">
    <h2 class="product-card__title">Overlap Lean</h2>
    <div class="product-card__body">
      <div class="product-card__photo photo--pale" role="img" aria-label="Photo of a pale overlap lean-to shed"></div>
      <div class="product-card__features"><h3>Product Features</h3><ul>
        <li>Fully Pressure Treated</li><li>Overlap Siding</li><li>Galvanised Nailed</li><li>Free Delivery &amp; Fitting</li><li>90lb Felt Roof Membrane</li></ul></div>
      <p class="product-card__price">From €339.00</p>
    </div>
  </article>

  <article class="product-card col-3 row-2">
    <h2 class="product-card__title">Kids Playhouse</h2>
    <div class="product-card__body">
      <div class="product-card__photo photo--warm" role="img" aria-label="Photo of a timber kids playhouse on a lawn"></div>
      <div class="product-card__features"><h3>Product Features</h3><ul>
        <li>Shiplap Siding</li><li>Arched Glazed windows</li><li>Stable Door</li><li>TimberTone Treated</li><li>90lb Felt Roof Membrane</li><li>Free Delivery &amp; Fitting</li></ul></div>
      <p class="product-card__price">From €449.99</p>
    </div>
  </article>

  <article class="product-card col-1 row-3">
    <h2 class="product-card__title">Premium Lodge</h2>
    <div class="product-card__body">
      <div class="product-card__photo photo--warm" role="img" aria-label="Photo of a long timber lodge shed"></div>
      <div class="product-card__features"><h3>Product Features</h3><ul>
        <li>Shiplap Siding</li><li>T&amp;G roof and floorng</li><li>Galavanised Fittings</li><li>TimberTone Treated</li><li>Free Home delivery</li></ul></div>
      <p class="product-card__price">From €599.99</p>
    </div>
  </article>

  <article class="product-card col-2 row-3">
    <h2 class="product-card__title">Overlap Standard</h2>
    <div class="product-card__body">
      <div class="product-card__photo photo--pale" role="img" aria-label="Photo of a pale overlap apex shed"></div>
      <div class="product-card__features"><h3>Product Features</h3><ul>
        <li>Overolap Siding</li><li>Fully Pressure treated</li><li>Free delivery &amp; fitting</li><li>Galvanised fittings &amp; fixings</li><li>Glazed windows</li></ul></div>
      <p class="product-card__price">From €399.99</p>
    </div>
  </article>

  <article class="product-card col-3 row-3">
    <h2 class="product-card__title">Kids Tree House</h2>
    <div class="product-card__body">
      <div class="product-card__photo photo--warm" role="img" aria-label="Photo of a raised timber kids tree house with steps"></div>
      <div class="product-card__features"><h3>Product Features</h3><ul>
        <li>Shiplap Siding</li><li>3ft Stand</li><li>Stable Door</li><li>TimberTone Treated</li><li>90lb Felt Roof Membrane</li><li>Free Delivery &amp; Fitting</li></ul></div>
      <p class="product-card__price">From €799.99</p>
    </div>
  </article>

  <article class="product-card col-1 row-4">
    <h2 class="product-card__title">Summer Chalet</h2>
    <div class="product-card__body">
      <div class="product-card__photo photo--warm" role="img" aria-label="Photo of a timber summer chalet with veranda"></div>
      <div class="product-card__features"><h3>Product Features</h3><ul>
        <li>18mm Shiplap Siding</li><li>T&amp;G Roof and Floor</li><li>Free Fitting &amp; Delivery</li><li>TimberTone Treated</li><li>Galavanised Nailed</li><li>30" Veranda</li></ul></div>
      <p class="product-card__price">From €629.00</p>
    </div>
  </article>

  <article class="product-card col-2 row-4">
    <h2 class="product-card__title">Overlap Kendal</h2>
    <div class="product-card__body">
      <div class="product-card__photo photo--pale" role="img" aria-label="Photo of a pale overlap Kendal shed in a yard"></div>
      <div class="product-card__features"><h3>Product Features</h3><ul>
        <li>Overlap Rustic Siding</li><li>Pressure treated</li><li>Galvanized fittings</li><li>Georgian style windows</li><li>Internal Membrane</li></ul></div>
      <p class="product-card__price">From €479.99</p>
    </div>
  </article>

  <div class="brand-mark"><span class="brand-mark__square"></span><span>Yard Huts 2 Go</span></div>
  <div class="partner-mark">TimberTone</div>
  <svg class="cert-badge" width="220" height="56" viewBox="0 0 220 56" role="img" aria-label="Certification badge">
    <rect x="0" y="0" width="220" height="56" rx="10" fill="#4f9a3a"/>
  </svg>

  <footer class="footer-band">CALL TODAY TO GET OUR LIFETIME WARRANTY</footer>
</main>
</body>
</html>
```